Our product is called "BrisaVeil Antimicrobial Photosensitizer Mask." It is worn over the face by individuals who have respiratory infections. It releases singlet oxygen upon contact with visible light. So, this product will be sold to the healthcare industry and in retail establishments to individuals with respiratory infections.
This website must have the look and feel of being professional and clean. So, a white background is where I think I want this website to end up. Though, I am open to designs that have different color backgrounds like a light to medium gray or black.. In other words I prefer a white background, but I do not want to constrain the artists who might have other unique ideas about how the website should appear.
The logo files are attached to this brief. #ff3e81 is the hex color code that is used in the mask. The green shade in the cloud and light rays surrounding the mask should be used as well.
Target Market(s)
Health and wellness
Industry/Entity Type
Healthcare
Coding
Number of Pages Required
5+ page
Requirements
Must have
- Pages: Home, Our Company, Contact, FAQ page, Order, Terms and Conditions, Legal

```html
<!DOCTYPE html>
<html lang="en">
<head>
<meta charset="utf-8">
<title>BrisaVeil Antimicrobial Photosensitizer Mask</title>
<link href="https://fonts.googleapis.com/css2?family=Noto+Serif:wght@400;500;600&family=Roboto:wght@400;500;700&display=swap" rel="stylesheet">
<style>
:root{
  --red:#c8202f;
  --red-dark:#a3182a;
  --red-bright:#e53a3a;
  --pink:#ff3e81;
  --green:#6a9a3f;
  --green-light:#b9dfa0;
  --ink:#111111;
  --text:#666666;
  --pale-pink:#fbeeee;
  --pale-cream:#f8f6ee;
  --white:#ffffff;
  --footer-bg:#f4f4f4;
}
*{margin:0;padding:0;box-sizing:border-box}
html,body{width:1200px;height:3775px;overflow:hidden}
body{position:relative;background:var(--white);font-family:"Roboto",Arial,sans-serif;color:var(--ink)}
.abs{position:absolute}
.serif{font-family:"Noto Serif",Georgia,serif}
.btn{position:absolute;display:flex;align-items:center;justify-content:center;gap:8px;color:var(--white);font-weight:700;font-size:14px;border-radius:24px;background:linear-gradient(90deg,var(--red-dark),var(--red-bright));text-transform:uppercase;border:2px solid rgba(255,255,255,.85)}
.btn-dot{width:13px;height:13px;border-radius:50%;background:var(--white);position:relative}
.btn-dot::after{content:"";position:absolute;left:4px;top:3px;border-left:5px solid var(--red);border-top:3.5px solid transparent;border-bottom:3.5px solid transparent}

/* hero */
.hero-photo{left:0;top:0;width:1200px;height:557px;background:
  radial-gradient(circle at 1120px 230px,rgba(240,190,120,.55) 0,rgba(240,190,120,0) 70px),
  radial-gradient(circle at 1010px 120px,rgba(230,200,150,.35) 0,rgba(230,200,150,0) 60px),
  radial-gradient(ellipse 190px 230px at 780px 190px,#a7c3d4 0,#7aa3bd 35%,rgba(90,130,155,0) 100%),
  radial-gradient(ellipse 320px 320px at 760px 330px,#3d6f93 0,rgba(40,80,110,0) 100%),
  radial-gradient(circle at 60px 420px,#4d6b72 0,rgba(60,90,100,0) 260px),
  linear-gradient(100deg,#32484f 0,#22343c 40%,#1c2c36 70%,#2a3a44 100%)}
.hero-wave{left:0;top:0;width:1200px;height:557px}
.nav{left:363px;top:19px;width:727px;height:72px;border-radius:36px;background:rgba(225,240,215,.85);border:2px solid rgba(255,255,255,.7);display:flex;align-items:center;padding-left:22px;gap:22px;font-size:14px;font-weight:500;text-transform:uppercase}
.nav a{color:var(--ink);text-decoration:none}
.nav a.active{color:var(--pink);text-decoration:underline}
.nav .nav-cta{margin-left:auto;margin-right:6px;height:52px;width:156px;border-radius:26px;background:linear-gradient(90deg,var(--red-dark),var(--red-bright));color:var(--white);display:flex;align-items:center;justify-content:center;font-weight:700}
.brand{left:60px;top:14px;width:320px;text-align:center}
.brand-mark{width:88px;height:88px;border-radius:50%;background:var(--green-light);margin:0 auto}
.brand-name{font-family:"Noto Serif",Georgia,serif;color:var(--red);font-size:11.5px;font-weight:600;margin-top:4px;white-space:nowrap}
.brand-tag{font-family:"Noto Serif",Georgia,serif;color:var(--red);font-size:8px;font-style:italic;margin-top:6px}
.hero-kicker{left:110px;top:164px;font-size:31px;color:var(--green-light);text-decoration:underline;text-underline-offset:4px;letter-spacing:.5px}
.hero-title{left:110px;top:204px;font-size:50px;line-height:64px;color:var(--white);font-weight:500}

/* about */
.about-photo{left:0;top:608px;width:527px;height:483px}
.section-title{font-size:47px;font-weight:500;color:var(--ink);letter-spacing:1px}
.about-title{left:602px;top:636px}
.about-copy{left:602px;top:713px;width:440px;font-size:15.5px;line-height:30px;color:var(--text)}
.about-copy p+p{margin-top:25px}

/* products */
.product-title{left:0;top:1198px;width:1200px;text-align:center}
.card{position:absolute;top:1276px;height:336px;background:var(--white);box-shadow:0 6px 22px rgba(0,0,0,.08);border-radius:6px}
.card-img{position:absolute;left:8px;top:9px;right:8px;height:239px;border-radius:3px}
.card-label{position:absolute;left:0;right:0;top:275px;text-align:center;font-size:20px;font-weight:700}
.card.featured{background:linear-gradient(180deg,var(--red-bright),var(--red))}
.card.featured .card-label{color:var(--white)}

/* benefits */
.benefits-bg{left:0;top:1660px;width:1200px;height:800px}
.benefits-title{left:107px;top:1793px}
.benefit{position:absolute;left:112px;width:500px;height:104px}
.benefit-icon{position:absolute;left:0;top:0;width:100px;height:100px;border-radius:50%;background:var(--white);box-shadow:0 4px 14px rgba(0,0,0,.12)}
.benefit-icon .in{position:absolute;left:9px;top:9px;width:82px;height:82px;border-radius:50%;display:flex;align-items:center;justify-content:center}
.benefit-icon .red{background:linear-gradient(135deg,var(--red-bright),var(--red-dark))}
.benefit-icon .grn{background:linear-gradient(135deg,#86b45a,var(--green))}
.benefit h3{position:absolute;left:125px;top:8px;font-size:16.5px;font-weight:500;text-transform:uppercase}
.benefit p{position:absolute;left:125px;top:35px;font-size:13.5px;line-height:26px;color:#333;width:360px}
.benefits-photo{left:650px;top:1811px;width:466px;height:466px;border-radius:50%;border:6px solid var(--white);box-shadow:0 8px 24px rgba(0,0,0,.15);background:
  radial-gradient(ellipse 90px 60px at 50% 46%,#dfe6ec 0,rgba(220,228,235,0) 100%),
  radial-gradient(ellipse 110px 140px at 50% 38%,#3a2e2a 0,rgba(50,40,36,0) 100%),
  radial-gradient(ellipse 80px 90px at 50% 80%,#8e8a86 0,rgba(140,135,130,0) 100%),
  radial-gradient(ellipse 200px 170px at 50% 100%,#1c2230 0,rgba(28,34,48,0) 100%),
  linear-gradient(180deg,#6c7078 0,#4a4e58 50%,#2e323c 100%)}

/* how it works */
.how-title{left:0;top:2405px;width:1200px;text-align:center}
.how-copy{left:270px;top:2475px;width:660px;text-align:center;font-size:15.5px;line-height:30px;color:var(--text)}
.step{position:absolute;top:2570px;width:180px;height:176px}
.step-label{position:absolute;top:2758px;width:200px;text-align:center;font-size:15px;font-weight:500;line-height:25px;text-transform:uppercase}
.step-label.on{color:var(--green)}
.arrow{position:absolute;top:2648px;width:22px;height:16px}

/* testimonials */
.testi-bg{left:0;top:2880px;width:1200px;height:520px}
.testi-title{left:0;top:2955px;width:1200px;text-align:center}
.testi{position:absolute;background:var(--white);box-shadow:0 6px 24px rgba(0,0,0,.08);border-radius:8px}
.avatar{position:absolute;border-radius:50%;background:
  radial-gradient(ellipse 30% 26% at 50% 36%,#8a6b5a 0,rgba(138,107,90,0) 100%),
  radial-gradient(ellipse 60% 45% at 50% 100%,#1b2330 0,rgba(27,35,48,0) 100%),
  linear-gradient(180deg,#7f8894,#3a4250)}
.testi h4{position:absolute;font-weight:700;text-transform:uppercase}
.testi .city{position:absolute;color:#333}
.testi p{position:absolute;color:var(--text)}
.testi.small h4{left:120px;top:44px;font-size:13px}
.testi.small .city{left:120px;top:64px;font-size:12px}
.testi.small .avatar{left:25px;top:18px;width:70px;height:70px}
.testi.small p{left:23px;top:100px;width:245px;font-size:11.5px;line-height:22px}
.testi.big h4{left:143px;top:46px;font-size:15.5px}
.testi.big .city{left:143px;top:72px;font-size:14px}
.testi.big .avatar{left:30px;top:20px;width:82px;height:82px}
.testi.big p{left:28px;top:120px;width:290px;font-size:14.5px;line-height:26px}
.slide-btn{position:absolute;top:3168px;width:52px;height:52px;border-radius:50%;background:var(--white);box-shadow:0 3px 12px rgba(0,0,0,.15);display:flex;align-items:center;justify-content:center;font-size:22px}

/* footer */
.footer-bg{left:0;top:3380px;width:1200px;height:395px}
.footer-brand{left:400px;top:3466px;width:400px;text-align:center}
.footer-brand .brand-mark{width:74px;height:74px}
.footer-brand .brand-name{font-size:13px}
.footer-nav{left:0;top:3630px;width:1200px;display:flex;justify-content:center;gap:22px;font-size:14px;font-weight:500;text-transform:uppercase}
.socials{left:545px;top:3674px;display:flex;gap:7px}
.socials span{width:32px;height:32px;border-radius:50%;background:#2a2a2a}
.socials span:first-child{background:var(--red)}
.copyright{left:0;top:3735px;width:1200px;text-align:center;font-size:14px;color:#222}
.bottom-line{left:0;top:3769px;width:1200px;height:6px;background:var(--red)}
</style>
</head>
<body>

<!-- HERO -->
<div class="abs hero-photo" role="img" aria-label="Photo of a woman wearing a blue surgical face mask in a softly lit clinic"></div>
<svg class="abs hero-wave" viewBox="0 0 1200 557" preserveAspectRatio="none">
  <path d="M0,440 C120,520 300,565 520,548 C760,528 950,360 1200,335 L1200,557 L0,557 Z" fill="var(--white)"/>
  <path d="M28,476 C150,540 330,575 560,550 C780,520 940,370 1160,336 C1000,340 820,470 640,515 C430,565 220,540 28,476 Z" fill="var(--red)"/>
</svg>

<nav class="abs nav">
  <a class="active">Home</a><a>About Us</a><a>How It Works</a><a>Healthcare Benefits</a><a>Product</a>
  <a class="nav-cta">Contact Us</a>
</nav>
<div class="abs brand">
  <div class="brand-mark"></div>
  <div class="brand-name">BrisaVeil Antimicrobial Photosensitizer Mask</div>
  <div class="brand-tag">"Powered by Light, Fueled by Air!"</div>
</div>
<div class="abs serif hero-kicker">BREATHABLE PROTECTION</div>
<div class="abs serif hero-title">LIGHT-ACTIVATED<br>DEFENSE</div>
<div class="btn" style="left:110px;top:359px;width:171px;height:45px">Shop Now <span class="btn-dot"></span></div>

<!-- ABOUT -->
<svg class="abs about-photo" viewBox="0 0 527 483" role="img" aria-label="Illustration of an open hand holding a glowing digital shield with a medical cross">
  <defs>
    <linearGradient id="aboutFill" x1="0" y1="0" x2="1" y2="1"><stop offset="0" stop-color="#3a7f90"/><stop offset=".55" stop-color="#173f4e"/><stop offset="1" stop-color="#0a1a22"/></linearGradient>
    <radialGradient id="aboutGlow" cx="0.55" cy="0.42" r="0.35"><stop offset="0" stop-color="#5fe3f0" stop-opacity=".75"/><stop offset=".5" stop-color="#2bb3c9" stop-opacity=".3"/><stop offset="1" stop-color="#2bb3c9" stop-opacity="0"/></radialGradient>
    <radialGradient id="aboutHand" cx="0.6" cy="0.75" r="0.3"><stop offset="0" stop-color="#9a8a80" stop-opacity=".55"/><stop offset="1" stop-color="#9a8a80" stop-opacity="0"/></radialGradient>
  </defs>
  <path d="M0,70 C90,10 260,-20 400,40 C520,95 540,260 470,380 C420,470 330,490 270,440 C200,380 120,400 0,380 Z" fill="#b9d9ad"/>
  <path d="M0,80 C90,25 250,5 380,55 C480,100 500,260 440,370 C395,455 330,470 275,425 C210,375 120,395 0,370 Z" fill="url(#aboutFill)"/>
  <path d="M0,80 C90,25 250,5 380,55 C480,100 500,260 440,370 C395,455 330,470 275,425 C210,375 120,395 0,370 Z" fill="url(#aboutGlow)"/>
  <path d="M0,80 C90,25 250,5 380,55 C480,100 500,260 440,370 C395,455 330,470 275,425 C210,375 120,395 0,370 Z" fill="url(#aboutHand)"/>
</svg>
<h2 class="abs serif section-title about-title">ABOUT US</h2>
<div class="abs about-copy">
  <p>Lorem ipsum dolor sit amet, consectetur adipiscing elit, sed do eiusmod tempor incididunt ut labore et dolore magna aliqua. Ut enim ad minim veniam, quis nostrud exercitation ullamco laboris nisi ut aliquip ex ea commodo consequat. Duis aute irure dolor in reprehenderit in voluptate velit esse cillum dol</p>
  <p>Lorem ipsum dolor sit amet, consectetur adipiscing elit, sed do eiusmod tempor incididunt ut labore et dolore magna aliqua. Ut enim ad minim veniam.</p>
</div>
<div class="btn" style="left:602px;top:1005px;width:171px;height:44px">Learn More <span class="btn-dot"></span></div>

<!-- PRODUCTS -->
<h2 class="abs serif section-title product-title">OUR PRODUCT</h2>
<div class="card" style="left:0;width:281px"><div class="card-img" style="left:0;background:radial-gradient(ellipse 70px 60px at 55% 62%,#eeeeec 0,rgba(235,235,232,0) 100%),radial-gradient(ellipse 110px 90px at 50% 30%,#6b4a36 0,rgba(100,70,50,0) 100%),linear-gradient(135deg,#9a9ca0,#4a4c52 60%,#2a2b30)" role="img" aria-label="Young man wearing a white face mask"></div><div class="card-label">LORUM IPSUM DOLOR</div></div>
<div class="card" style="left:300px;width:290px"><div class="card-img" style="background:radial-gradient(ellipse 40px 30px at 50% 42%,#ffffff 0,rgba(255,255,255,0) 100%),radial-gradient(ellipse 60px 100px at 50% 35%,#4a3a40 0,rgba(74,58,64,0) 100%),radial-gradient(ellipse 110px 60px at 50% 95%,#8e8c8e 0,rgba(142,140,142,0) 100%),linear-gradient(135deg,#f0f0f1,#c9c8cb)" role="img" aria-label="Woman in a grey blazer wearing a white face mask"></div><div class="card-label">LORUM IPSUM DOLOR</div></div>
<div class="card featured" style="left:608px;width:292px"><div class="card-img" style="background:radial-gradient(ellipse 70px 50px at 50% 62%,#141414 0,rgba(20,20,20,0) 100%),radial-gradient(ellipse 100px 70px at 50% 18%,#1a1a1a 0,rgba(26,26,26,0) 100%),radial-gradient(ellipse 80px 60px at 50% 45%,#b08470 0,rgba(176,132,112,0) 100%),linear-gradient(135deg,#a89a8e,#5b4e46 60%,#2f2926)" role="img" aria-label="Woman in a black beanie wearing a black face mask"></div><div class="card-label">LORUM IPSUM DOLOR</div></div>
<div class="card" style="left:917px;width:283px"><div class="card-img" style="right:0;background:radial-gradient(ellipse 140px 40px at 60% 6%,#f2c418 0,rgba(242,196,24,0) 100%),radial-gradient(ellipse 70px 55px at 55% 62%,#cfe0ee 0,rgba(207,224,238,0) 100%),linear-gradient(135deg,#4f8fc0,#8fb6d2 45%,#e2ebf2)" role="img" aria-label="Worker in a yellow hard hat wearing goggles and a respirator mask"></div><div class="card-label">LORUM IPSUM DOLOR</div></div>

<!-- BENEFITS -->
<svg class="abs benefits-bg" viewBox="0 0 1200 800" preserveAspectRatio="none">
  <path d="M0,240 C200,120 420,60 620,40 C820,20 1000,60 1200,120 L1200,580 C1120,780 960,800 900,650 C840,520 600,640 300,660 C160,670 60,640 0,620 Z" fill="var(--pale-pink)"/>
  <path d="M0,240 C200,180 380,190 560,260 L560,640 C400,660 200,670 0,610 Z" fill="var(--pale-cream)" opacity=".8"/>
</svg>
<h2 class="abs serif section-title benefits-title">PRODUCT BENEFITS</h2>

<div class="benefit" style="top:1896px">
  <div class="benefit-icon"><div class="in red"><svg width="46" height="46" viewBox="0 0 46 46" fill="none" stroke="#fff" stroke-width="2.5" stroke-linecap="round"><path d="M8,16 C16,10 30,10 38,16 L38,28 C30,36 16,36 8,28 Z"/><path d="M14,20h18M14,25h18M3,18l5,2M43,18l-5,2"/></svg></div></div>
  <h3>Light-Activated Defense</h3>
  <p>Lorem ipsum dolor sit amet, consectetur adipiscing elit, sed do eiusmod tempor incididunt</p>
</div>
<div class="benefit" style="top:2030px">
  <div class="benefit-icon"><div class="in grn"><svg width="46" height="46" viewBox="0 0 46 46" fill="none" stroke="#fff" stroke-width="2.5" stroke-linecap="round" stroke-linejoin="round"><path d="M20,8 L34,13 L34,24 C34,33 27,38 20,40 C13,38 6,33 6,24 L6,13 Z"/><path d="M13,24 l5,5 l9,-10"/></svg></div></div>
  <h3>Comfortable &amp; Breathable Design</h3>
  <p>Lorem ipsum dolor sit amet, consectetur adipiscing elit, sed do eiusmod tempor incididunt</p>
</div>
<div class="benefit" style="top:2166px">
  <div class="benefit-icon"><div class="in red"><svg width="46" height="46" viewBox="0 0 46 46" fill="none" stroke="#fff" stroke-width="2.5" stroke-linecap="round" stroke-linejoin="round"><circle cx="23" cy="12" r="6"/><path d="M10,36 C10,26 16,22 23,22 C30,22 36,26 36,36 Z"/><path d="M19,30 l3,3 l6,-6"/></svg></div></div>
  <h3>Scientifically Proven</h3>
  <p>Lorem ipsum dolor sit amet, consectetur adipiscing elit, sed do eiusmod tempor incididunt</p>
</div>
<div class="abs benefits-photo" role="img" aria-label="Woman in a dark coat wearing a white face mask in a crowd"></div>

<!-- HOW IT WORKS -->
<h2 class="abs serif section-title how-title">HOW IT WORKS</h2>
<p class="abs how-copy">Lorem ipsum dolor sit amet, consectetur adipiscing elit, sed do eiusmod tempor incididunt ut labore et dolore magna aliqua. Ut enim ad minim veniam</p>

<svg class="step" style="left:137px" viewBox="0 0 180 176" fill="none">
  <path d="M55,14 H125 L170,88 L125,162 H55 L10,88 Z" fill="#fff" stroke="#f1ece0" stroke-width="4" stroke-linejoin="round"/>
  <path d="M60,14 H120 V42 L90,50 L60,42 Z" fill="var(--green)"/>
  <g stroke="var(--red)" stroke-width="3" stroke-linecap="round"><circle cx="90" cy="100" r="30" stroke-dasharray="24 14"/><path d="M76,100 l10,10 l20,-22"/><circle cx="90" cy="70" r="5"/><circle cx="90" cy="130" r="5"/><circle cx="60" cy="100" r="5"/><circle cx="120" cy="100" r="5"/></g>
</svg>
<svg class="arrow" style="left:344px" viewBox="0 0 22 16" fill="none" stroke="var(--red)" stroke-width="2.5"><path d="M2,2 l7,6 l-7,6 M12,2 l7,6 l-7,6"/></svg>
<svg class="step" style="left:388px" viewBox="0 0 180 176" fill="none">
  <path d="M55,14 H125 L170,88 L125,162 H55 L10,88 Z" fill="#fff" stroke="#f1ece0" stroke-width="4" stroke-linejoin="round"/>
  <path d="M60,14 H120 V42 L90,50 L60,42 Z" fill="var(--red)"/>
  <g stroke="var(--red)" stroke-width="3" stroke-linecap="round" stroke-linejoin="round"><path d="M58,80 C70,66 110,66 122,80 L122,112 C110,132 70,132 58,112 Z"/><path d="M90,70 V128 M62,92 H118"/></g>
</svg>
<svg class="arrow" style="left:588px" viewBox="0 0 22 16" fill="none" stroke="var(--red)" stroke-width="2.5"><path d="M2,2 l7,6 l-7,6 M12,2 l7,6 l-7,6"/></svg>
<svg class="step" style="left:635px" viewBox="0 0 180 176" fill="none">
  <path d="M55,14 H125 L170,88 L125,162 H55 L10,88 Z" fill="#fff" stroke="#f1ece0" stroke-width="4" stroke-linejoin="round"/>
  <path d="M60,14 H120 V42 L90,50 L60,42 Z" fill="var(--green)"/>
  <g stroke="var(--red)" stroke-width="3" stroke-linecap="round"><path d="M88,68 C70,62 58,76 62,88 C52,96 56,114 68,116 C70,128 84,132 88,124 Z"/><path d="M92,68 C110,62 122,76 118,88 C128,96 124,114 112,116 C110,128 96,132 92,124 Z"/><path d="M70,90 h10 M100,90 h12 M74,106 h10 M98,106 h10"/></g>
</svg>
<svg class="arrow" style="left:834px" viewBox="0 0 22 16" fill="none" stroke="var(--red)" stroke-width="2.5"><path d="M2,2 l7,6 l-7,6 M12,2 l7,6 l-7,6"/></svg>
<svg class="step" style="left:884px" viewBox="0 0 180 176" fill="none">
  <path d="M55,14 H125 L170,88 L125,162 H55 L10,88 Z" fill="#fff" stroke="#f1ece0" stroke-width="4" stroke-linejoin="round"/>
  <path d="M60,14 H120 V42 L90,50 L60,42 Z" fill="var(--red)"/>
  <g stroke="var(--red)" stroke-width="3" stroke-linecap="round" stroke-linejoin="round"><path d="M90,132 L62,104 C48,90 56,68 74,70 C82,71 88,78 90,82 C92,78 98,71 106,70 C124,68 132,90 118,104 Z"/><path d="M38,100 H72 L78,88 L88,114 L96,94 L102,100 H142"/></g>
</svg>

<div class="step-label" style="left:127px">Activating with<br>light</div>
<div class="step-label" style="left:378px">Release of singlet<br>oxygen</div>
<div class="step-label on" style="left:631px">Continuous<br>protection</div>
<div class="step-label" style="left:884px">Living with long<br>health</div>

<!-- TESTIMONIALS -->
<svg class="abs testi-bg" viewBox="0 0 1200 520" preserveAspectRatio="none">
  <path d="M0,60 C250,20 500,60 700,90 C900,120 1050,80 1200,30 L1200,520 L0,520 Z" fill="var(--pale-cream)" opacity=".7"/>
  <path d="M500,200 C700,150 950,180 1200,160 L1200,520 L700,520 Z" fill="var(--pale-pink)" opacity=".7"/>
</svg>
<h2 class="abs serif section-title testi-title">OUR TESTIMONIALS</h2>
<div class="slide-btn" style="left:34px">«</div>
<div class="slide-btn" style="left:1114px;color:var(--red)">»</div>

<div class="testi small" style="left:114px;top:3079px;width:286px;height:229px">
  <div class="avatar" role="img" aria-label="Portrait of a customer in a suit"></div>
  <h4>Reza Tamlin</h4><div class="city">Lorum Ipsum City</div>
  <p>Lorem ipsum dolor sit amet, consectetur adipisc ing elit, sed do eiusmod tempor incididunt ut labore et dolore magna aliqua. Ut enim ad minim veniam, quis nostrud exercitation ullamco laboris.</p>
</div>
<div class="testi big" style="left:431px;top:3059px;width:338px;height:269px">
  <div class="avatar" role="img" aria-label="Portrait of a customer in a suit"></div>
  <h4>Reza Tamlin</h4><div class="city">Lorum Ipsum City</div>
  <p>Lorem ipsum dolor sit amet, consectetur adipisc ing elit, sed do eiusmod tempor incididunt ut labore et dolore magna aliqua. Ut enim ad minim veniam, quis nostrud exercitation ullamco laboris.</p>
</div>
<div class="testi small" style="left:800px;top:3079px;width:286px;height:229px">
  <div class="avatar" role="img" aria-label="Portrait of a customer in a suit"></div>
  <h4>Reza Tamlin</h4><div class="city">Lorum Ipsum City</div>
  <p>Lorem ipsum dolor sit amet, consectetur adipisc ing elit, sed do eiusmod tempor incididunt ut labore et dolore magna aliqua. Ut enim ad minim veniam, quis nostrud exercitation ullamco laboris.</p>
</div>

<!-- FOOTER -->
<svg class="abs footer-bg" viewBox="0 0 1200 395" preserveAspectRatio="none">
  <path d="M0,40 C200,120 300,160 420,110 C600,40 850,20 1200,20 L1200,395 L0,395 Z" fill="var(--footer-bg)"/>
  <path d="M60,215 C180,240 230,200 300,120 C360,60 470,40 620,50 C800,60 950,110 1180,30 C960,140 800,90 640,80 C480,70 380,90 330,150 C260,230 170,250 60,215 Z" fill="var(--red)"/>
</svg>
<div class="abs brand footer-brand">
  <div class="brand-mark"></div>
  <div class="brand-name">BrisaVeil Antimicrobial Photosensitizer Mask</div>
  <div class="brand-tag">"Powered by Light, Fueled by Air!"</div>
</div>
<nav class="abs footer-nav"><span>Home</span><span>About Us</span><span>How It Works</span><span>Healthcare Benefits</span><span>Product</span><span>Contact Us</span></nav>
<div class="abs socials"><span></span><span></span><span></span></div>
<div class="abs copyright">Copyright2024.All Rights Reserved</div>
<div class="abs bottom-line"></div>

</body>
</html>
```